Clean and modern business cards

Looking for an updated business card design for my dental office “corvanta dental” . Looking for a modern clean / sleek design . I’m thinking black background but open to seeing other options . One side needs to have an appointment card . Card needs to have logo, dentist name , phone, email , address . I’ve attached couple of cards I thought were cool as well as my logo
Target Market(s)
Dental patients
Industry/Entity Type
Dentistry
Contact Information for Business Card
Phone email address

```html
<!DOCTYPE html>
<html lang="en">
<head>
<meta charset="utf-8">
<title>Corvanta Dental – Business Cards</title>
<link rel="stylesheet" href="https://fonts.googleapis.com/css2?family=Montserrat:wght@400;500;700;800&family=Roboto+Condensed:wght@400&family=Roboto:wght@400&display=swap">
<style>
  :root {
    --page-bg: #2b2b2c;
    --card-bg: #202021;
    --card-bg-light: #2a2a2b;
    --white: #ffffff;
    --soft-white: #e6e6e6;
    --field-bg: #ededed;
    --ink: #1d1d1d;
    --lime: #9cc21c;
    --plum: #8c1f6e;
    --plum-clear: rgba(140, 31, 110, 0);
  }
  * { margin: 0; padding: 0; box-sizing: border-box; }
  html, body { width: 1200px; height: 1138px; overflow: hidden; }
  body {
    background: var(--page-bg);
    font-family: "Montserrat", sans-serif;
    position: relative;
  }
  .card {
    position: absolute;
    width: 621px;
    height: 375px;
    border-radius: 16px;
    overflow: hidden;
    background: linear-gradient(135deg, var(--card-bg-light), var(--card-bg));
    box-shadow: 0 8px 18px rgba(0,0,0,.45);
  }
  .card--appointment { left: 274px; top: 186px; }
  .card--contact { left: 276px; top: 608px; }

  .brand-name {
    position: absolute;
    color: var(--white);
    font-weight: 700;
    line-height: 1;
    text-align: right;
  }
  .brand-name .word-main { display: block; font-size: 41px; letter-spacing: 0; }
  .brand-name .word-sub {
    display: block; font-size: 17px; font-weight: 500;
    letter-spacing: .3em; margin-right: -.3em; margin-top: 9px;
  }
  .card--appointment .brand-name { left: 28px; top: 101px; }

  .emboss-art {
    position: absolute;
    right: 0; top: 0;
    width: 330px; height: 280px;
    background: radial-gradient(circle at 55% 45%, #3a3a3b 0%, #262627 60%, rgba(32,32,33,0) 100%);
  }

  .appt-label {
    position: absolute; left: 24px; top: 259px;
    color: var(--soft-white); font-size: 17px; font-weight: 400;
  }
  .appt-field {
    position: absolute; left: 24px; top: 288px;
    width: 577px; height: 44px;
    background: linear-gradient(90deg, #d9d9d9, var(--field-bg) 40%, #f7f7f7);
    display: flex; align-items: flex-end; gap: 6px;
    padding: 0 12px 7px;
    font-family: "Roboto", sans-serif; font-size: 17px; color: var(--ink);
  }
  .appt-field .line { border-bottom: 1.5px solid var(--ink); height: 1px; margin-bottom: 3px; }
  .appt-field .line--date { width: 242px; margin-right: 2px; }
  .appt-field .line--time { width: 210px; }
  .appt-note {
    position: absolute; left: 24px; top: 336px;
    font-family: "Roboto Condensed", sans-serif;
    color: var(--soft-white); font-size: 15.8px; white-space: nowrap;
  }

  .card--contact .brand-mark {
    position: absolute; left: 26px; top: 44px;
    width: 140px; height: 140px; border-radius: 50%;
    background: var(--plum);
  }
  .card--contact .brand-name { left: 180px; top: 80px; }

  .wave-band {
    position: absolute; left: 0; top: 160px;
    width: 621px; height: 215px;
    background: linear-gradient(160deg, var(--plum-clear) 30%, var(--plum) 70%);
  }

  .dentist { position: absolute; left: 46px; top: 201px; }
  .dentist-name { color: var(--lime); font-weight: 800; font-size: 23px; line-height: 1.1; }
  .dentist-credentials { color: var(--soft-white); font-size: 16px; margin-top: 4px; }

  .contact-list {
    position: absolute; right: 26px; top: 230px;
    list-style: none; text-align: right;
    color: var(--white); font-size: 16px;
  }
  .contact-list li { display: flex; justify-content: flex-end; align-items: center; gap: 12px; height: 24px; }
  .contact-list svg { width: 15px; height: 15px; }
  .address {
    position: absolute; right: 22px; top: 306px;
    color: var(--white); font-size: 16px; text-align: right; line-height: 25px;
    font-style: normal;
  }
</style>
</head>
<body>

<section class="card card--appointment">
  <div class="emboss-art" role="img" aria-label="Embossed decorative bubble pattern"></div>
  <div class="brand-name"><span class="word-main">CORVANTA</span><span class="word-sub">DENTAL</span></div>
  <p class="appt-label">Your Next Appointment is:</p>
  <div class="appt-field">
    <span>Date:</span><span class="line line--date"></span>
    <span>Time:</span><span class="line line--time"></span>
  </div>
  <p class="appt-note">To cancel/reschedule please notify us at least 48 hours prior to your scheduled appointment</p>
</section>

<section class="card card--contact">
  <div class="wave-band" role="img" aria-label="Decorative colour wave band along the lower edge"></div>
  <div class="brand-mark"></div>
  <div class="brand-name"><span class="word-main">CORVANTA</span><span class="word-sub">DENTAL</span></div>
  <div class="dentist">
    <p class="dentist-name">DR BELARIN</p>
    <p class="dentist-credentials">Bsc (dent) DMD</p>
  </div>
  <ul class="contact-list">
    <li>204-555-0192
      <svg viewBox="0 0 16 16"><path fill="#fff" d="M2 6c0-2 3-3 6-3s6 1 6 3v1h-3V6H5v1H2z M4 8h8l1 5H3z"/></svg></li>
    <li>www.corvantadental.ca
      <svg viewBox="0 0 16 16"><path d="M1 3h14v10H1z M2 4l6 5 6-5" fill="none" stroke="#fff" stroke-width="1.4"/></svg></li>
    <li>hello@corvantadental.ca
      <svg viewBox="0 0 16 16"><circle cx="8" cy="8" r="6.5" fill="none" stroke="#fff" stroke-width="1.3"/><path d="M1.5 8h13M8 1.5c-3 3-3 10 0 13M8 1.5c3 3 3 10 0 13" fill="none" stroke="#fff" stroke-width="1.1"/></svg></li>
  </ul>
  <address class="address">210–4870 Marlowe<br>HWY, Winnipeg, MB R2K 3T5</address>
</section>

</body>
</html>
```